School Signage

I am wanting designs for signs completed that prompt students of the school requirements for hats, preparation and play.

I've uploaded rough examples of what we're after, but we would like them stylised and better than the example, including:
- A stylised logo/graphic for the 'Wallumba 1, 2, 3'
- Clear, crisp signage for the words.
- Graphics that reinforce the message of the sign.

We're after three signs:
- One that will be located on the oval to prompt hat use.
- One that will be near the entry prompting the morning routine (please make this one landscape with instructions for 'on time' on one side, and 'late' on the other).
- One that will be located within the school prompting readiness for class.

```html
<!DOCTYPE html>
<html lang="en">
<head>
<meta charset="utf-8">
<title>Wallumba Signage Set</title>
<link href="https://fonts.googleapis.com/css2?family=Montserrat:wght@400;500;600;700;800&display=swap" rel="stylesheet">
<style>
:root{
  --backdrop:#8eaed8;
  --green:#0c4a12;
  --green-deep:#083a0e;
  --yellow:#ffe600;
  --yellow-soft:#fff3a0;
  --white:#ffffff;
  --ink:#111111;
  --grey:#9a9a9a;
  --bell-a:#ffd36a;
  --bell-b:#e9a23a;
}
*{box-sizing:border-box;margin:0;padding:0}
html,body{width:1200px;height:642px;overflow:hidden}
body{background:var(--backdrop);font-family:"Montserrat",sans-serif;position:relative}
.sign{position:absolute;top:82px;width:338px;height:477px;background:var(--white);box-shadow:0 22px 30px rgba(40,70,120,.35);overflow:hidden}
.sign--ready{left:81px}
.sign--hats{left:430px}
.sign--routine{left:781px}
.sign__header{position:absolute;left:0;top:0;width:338px;height:108px}
.sign__header svg{position:absolute;left:0;top:0}
.sign__title{position:absolute;left:30px;color:var(--yellow);font-weight:800;line-height:.95;letter-spacing:-.5px}
.sign--ready .sign__title{top:15px;font-size:33px}
.sign__subtitle{position:absolute;left:30px;top:82px;color:var(--white);font-size:13px;font-weight:500;letter-spacing:-.3px}
.sign--hats .sign__title{top:30px;left:24px;font-size:45px}
.sign--routine .sign__title{top:22px;left:23px;font-size:29px;line-height:1}
.brand{position:absolute;right:16px;top:30px;width:84px;display:flex;flex-direction:column;align-items:center;gap:4px}
.brand__dot{width:26px;height:26px;border-radius:50%;background:var(--yellow)}
.brand__name{color:var(--green);font-weight:800;font-size:13px}
.sign__heading{position:absolute;left:0;width:100%;text-align:center;color:var(--green);font-weight:800;letter-spacing:-.6px;line-height:1.2}
.sign--ready .sign__heading{top:133px;font-size:21px;padding-left:15px}
.sign--hats .sign__heading{top:128px;font-size:20.5px}
.sign--routine .sign__heading{top:120px;font-size:24px}
.sign__bar{position:absolute;background:var(--yellow);color:var(--ink);font-weight:500;font-size:16px;display:flex;align-items:center;justify-content:center;letter-spacing:-.4px;border-radius:2px}
.sign--ready .sign__bar{left:44px;top:173px;width:254px;height:34px}
.sign--hats .sign__bar{left:42px;top:184px;width:253px;height:34px}
.sign--routine .sign__bar{left:72px;top:153px;width:195px;height:34px}
.item{position:absolute;border:1.5px solid var(--yellow-soft);border-radius:6px;display:flex;align-items:center;background:var(--white)}
.item__num{position:absolute;top:-1px;right:-1px;background:var(--yellow);color:var(--ink);font-weight:700;font-size:13px;padding:5px 5px;border-radius:5px}
.sign--ready .item{left:44px;width:254px;height:58px}
.sign--ready .item__icon{width:56px;margin-left:14px;display:flex;justify-content:center}
.sign--ready .item__label{margin-left:10px;font-size:15px;font-weight:500;letter-spacing:-.4px;color:var(--ink);line-height:1.2}
.sign--hats .item{height:58px;border-color:var(--yellow)}
.sign--hats .item--sitting{border-color:var(--grey)}
.sign--hats .item--sitting .item__num{right:auto;left:-1px;background:var(--green);color:var(--white)}
.figure{width:28px;height:42px;border-radius:6px;background:var(--green);margin-left:32px}
.sign--hats .item__label{margin-left:18px;font-size:27px;font-weight:500;color:var(--ink);letter-spacing:-.5px}
.routine-box{position:absolute;left:23px;top:196px;width:201px;height:122px;border:1.5px solid var(--yellow-soft);border-radius:3px;padding:10px 10px}
.routine-box__title{color:var(--green);font-weight:700;font-size:13px;letter-spacing:-.3px;margin-bottom:7px}
.step{display:flex;align-items:flex-start;gap:8px;font-size:9.5px;letter-spacing:-.4px;line-height:1.2;margin-bottom:7px;color:var(--ink)}
.step svg{flex:none;margin-top:0}
.late-box{position:absolute;left:118px;top:329px;width:201px;height:125px;background:var(--green-deep);padding:10px 12px}
.late-box .routine-box__title{color:var(--yellow)}
.late-box .step{color:var(--white)}
.motto{position:absolute;left:180px;top:202px;transform:rotate(-5deg);transform-origin:left top;color:var(--green);font-weight:800;font-size:14px;line-height:1.45}
.motto span{background:var(--yellow);padding:0 3px}
.bell{position:absolute;left:50px;top:340px;width:72px;height:84px;border-radius:40px 40px 14px 14px;background:radial-gradient(circle at 40% 35%,var(--bell-a),var(--bell-b))}
</style>
</head>
<body>

<section class="sign sign--ready">
  <header class="sign__header">
    <svg width="338" height="108" viewBox="0 0 338 108"><path d="M0 0H338V108H252C230 80 222 40 220 0Z" fill="var(--green)"/><path d="M222 0C226 45 240 85 262 108H338V0Z" fill="var(--white)"/></svg>
    <h1 class="sign__title">Curiosity<br>&amp; Drive</h1>
    <p class="sign__subtitle">Wallumba Learner Values</p>
    <div class="brand"><span class="brand__dot"></span><span class="brand__name">Wallumba</span></div>
  </header>
  <h2 class="sign__heading">Are you ready for class?</h2>
  <div class="sign__bar">The Wallumba 1, 2, 3</div>
  <div class="item" style="top:225px">
    <span class="item__icon"><svg width="52" height="38" viewBox="0 0 52 38"><rect x="7" y="2" width="38" height="26" rx="2" fill="none" stroke="var(--green)" stroke-width="4"/><path d="M1 31H51L47 37H5Z" fill="var(--green)"/></svg></span>
    <span class="item__label">Laptop/workbook</span><span class="item__num">01</span>
  </div>
  <div class="item" style="top:294px">
    <span class="item__icon"><svg width="30" height="46" viewBox="0 0 30 46"><rect x="5" y="0" width="14" height="10" rx="2" fill="var(--green)"/><rect x="3" y="8" width="20" height="36" rx="5" fill="var(--green)" transform="rotate(-12 13 26)"/></svg></span>
    <span class="item__label">Phone in Lockpod</span><span class="item__num">02</span>
  </div>
  <div class="item" style="top:361px">
    <span class="item__icon"><svg width="50" height="36" viewBox="0 0 50 36"><path d="M8 28C8 10 18 2 28 2S46 10 46 26Z" fill="var(--green)"/><path d="M2 32C10 26 24 26 46 26L42 34C28 32 14 32 2 32Z" fill="var(--green)"/></svg></span>
    <span class="item__label">Correct uniform<br>(including hat)</span><span class="item__num">03</span>
  </div>
</section>

<section class="sign sign--hats">
  <header class="sign__header">
    <svg width="338" height="108" viewBox="0 0 338 108"><path d="M0 0H338V108H252C230 80 222 40 220 0Z" fill="var(--green)"/><path d="M222 0C226 45 240 85 262 108H338V0Z" fill="var(--white)"/></svg>
    <h1 class="sign__title">Integrity</h1>
    <div class="brand"><span class="brand__dot"></span><span class="brand__name">Wallumba</span></div>
  </header>
  <h2 class="sign__heading">We wear hats at Wallumba<br>when outdoors...</h2>
  <div class="sign__bar">The Wallumba 1, 2, 3</div>
  <div class="item" style="left:76px;top:237px;width:231px">
    <span class="figure" role="img" aria-label="Walking person pictogram"></span>
    <span class="item__label">Walking</span><span class="item__num">01</span>
  </div>
  <div class="item item--sitting" style="left:31px;top:308px;width:230px">
    <span class="figure" style="margin-left:68px" role="img" aria-label="Sitting person pictogram"></span>
    <span class="item__label">Sitting</span><span class="item__num">02</span>
  </div>
  <div class="item" style="left:76px;top:377px;width:231px">
    <span class="figure" role="img" aria-label="Person playing with a ball pictogram"></span>
    <span class="item__label">Playing</span><span class="item__num">03</span>
  </div>
</section>

<section class="sign sign--routine">
  <header class="sign__header">
    <svg width="338" height="108" viewBox="0 0 338 108"><path d="M0 0H338V108H252C230 80 222 40 220 0Z" fill="var(--green)"/><path d="M222 0C226 45 240 85 262 108H338V0Z" fill="var(--white)"/></svg>
    <h1 class="sign__title">Exceed Your<br>Expectations</h1>
    <div class="brand"><span class="brand__dot"></span><span class="brand__name">Wallumba</span></div>
  </header>
  <h2 class="sign__heading">Morning Routine</h2>
  <div class="sign__bar">The Wallumba 1, 2, 3</div>
  <div class="routine-box">
    <p class="routine-box__title">On Time:</p>
    <p class="step"><svg width="12" height="12" viewBox="0 0 12 12"><circle cx="6" cy="6" r="5" fill="none" stroke="var(--green)" stroke-width="2"/><path d="M6 3V6H8" stroke="var(--green)" fill="none"/></svg>1. Arrive before 8:30 AM</p>
    <p class="step"><svg width="12" height="12" viewBox="0 0 12 12"><rect x="0" y="0" width="12" height="12" fill="var(--green)"/><path d="M4 0V12M8 0V12" stroke="var(--white)"/></svg>2. Drop bag at locker and<br>collect learning materials</p>
    <p class="step"><svg width="12" height="12" viewBox="0 0 12 12"><rect x="1" y="2" width="10" height="10" rx="3" fill="var(--green)"/><rect x="4" y="0" width="4" height="3" fill="var(--green)"/></svg>3. Arrive at Home Group<br>House Assembly before 8:40 AM</p>
  </div>
  <p class="motto"><span>Early is on Time,</span><br><span>on time is late</span></p>
  <div class="bell" role="img" aria-label="Golden school bell illustration"></div>
  <div class="late-box">
    <p class="routine-box__title">Running Late:</p>
    <p class="step"><svg width="12" height="12" viewBox="0 0 12 12"><circle cx="6" cy="6" r="5" fill="none" stroke="var(--yellow)" stroke-width="2"/><path d="M6 3V6H8" stroke="var(--yellow)" fill="none"/></svg>1. Arrive before 8:30 AM</p>
    <p class="step"><svg width="12" height="12" viewBox="0 0 12 12"><rect x="0" y="0" width="12" height="12" fill="var(--yellow)"/><path d="M4 0V12M8 0V12" stroke="var(--green-deep)"/></svg>2. Drop bag at locker and<br>collect learning materials</p>
    <p class="step"><svg width="12" height="12" viewBox="0 0 12 12"><rect x="1" y="2" width="10" height="10" rx="3" fill="var(--yellow)"/><rect x="4" y="0" width="4" height="3" fill="var(--yellow)"/></svg>3. Arrive at Home Group<br>House Assembly before 8:40 AM</p>
  </div>
</section>

</body>
</html>
```